Scriva Docs and Scriva Slides template creation using existing logo as style guide

Create a professional looking Scriva Docs document template and Scriva Slides template for Korvath Advisory Pty Ltd using a logo that's already been created as the style guide. Korvath is a professional services business providing strategy, governance and execution support to small and medium business, Boards and executive teams. refer design brief.

Target Market(s)

Small to medium business, Chairs, Boards, executive teams, general managers

Industry/Entity Type

Professional business services, consultancy, business support outsourcing

Font styles to use
Other font styles liked:
• calibri

Requirements
Must have
• leverage the existing logo for colour scheme. Use the KORVATH logo type font. Fully editable templates Word and Scriva Slides,
Nice to have
• Refer to the design brief
Should not have
• animations, cartoons, stock images of people.

```html
<!DOCTYPE html>
<html lang="en">
<head>
<meta charset="utf-8">
<title>Korvath Advisory – Document and Slide Templates</title>
<link href="https://fonts.googleapis.com/css2?family=Montserrat:wght@300;400;500;600;700&display=swap" rel="stylesheet">
<style>
:root{
  --navy:#1d2f45;
  --charcoal:#4b4d50;
  --grey:#8a8c8f;
  --mist:#d3d6da;
  --paper:#ffffff;
  --canvas:#d7d9d3;
  --gold:#c9a468;
  --sheet:#e7e8ea;
  --tile-slides:#e8553f;
  --tile-docs:#2a64c4;
}
*{margin:0;padding:0;box-sizing:border-box}
html,body{width:1200px;height:1200px;overflow:hidden}
body{background:var(--canvas);position:relative;font-family:"Montserrat",sans-serif;color:var(--navy)}
.slide{position:absolute;width:165px;height:93px;box-shadow:2px 3px 5px rgba(0,0,0,.18)}
.slide text{font-family:"Montserrat",sans-serif;fill:var(--navy)}
.lb{font-size:4px;font-weight:600;letter-spacing:1.2px}
.tt{font-size:10.5px;font-weight:500}
.ft{font-size:5px;font-weight:600;letter-spacing:1.4px}
.sm{font-size:3.5px;font-weight:600}
.xs{font-size:2.8px;font-weight:500}
.num{font-size:13px;font-weight:300}
.mark{font-weight:500}
.light text,.slide .w{fill:#fff}
.bar{fill:var(--mist)}
.dbar{fill:#4c5d72}

.brand-block{position:absolute;left:40px;top:716px;width:560px;text-align:right}
.brand-name{font-weight:500;font-size:80px;letter-spacing:.08em;margin-right:-.08em;line-height:1;color:var(--navy)}
.brand-tagline{font-weight:400;font-size:24px;letter-spacing:.04em;line-height:1.4;margin-top:34px;color:var(--navy)}
.headline{font-weight:600;font-size:43px;line-height:1.18;margin-top:26px;color:var(--navy)}
.app-tiles{position:absolute;left:360px;top:1040px;display:flex;gap:46px;align-items:center}
.app-tile{display:flex;align-items:center;gap:12px;font-weight:600;font-size:20px;color:var(--navy)}
.app-tile .dot{width:58px;height:58px;border-radius:50%;background:var(--tile-slides)}
.app-tile .sq{width:58px;height:58px;background:var(--tile-docs)}

.letterhead{position:absolute;left:745px;top:688px;width:360px;height:496px;background:var(--sheet);box-shadow:4px 6px 14px rgba(0,0,0,.25);overflow:hidden}
.lh-head{height:104px;background:var(--navy);color:#fff;position:relative}
.lh-logo{position:absolute;left:34px;top:30px;text-align:left}
.lh-logo .name{font-weight:500;font-size:22px;letter-spacing:.08em}
.lh-logo .tag{font-size:6px;letter-spacing:.04em;line-height:1.5;margin-top:5px}
.lh-person{position:absolute;right:26px;top:38px;text-align:left}
.lh-person .pn{font-weight:700;font-size:13px}
.lh-person .pr{font-size:9.5px;margin-top:1px}
.lh-person .ph{font-size:6px;margin-top:6px;display:flex;gap:6px;align-items:center}
.lh-body{padding:22px 30px 0 30px;font-size:6px;line-height:1.55;color:#26303c}
.lh-addr{font-style:italic}
.lh-addr strong{font-style:normal}
.lh-date{text-align:right;margin-top:-8px}
.lh-body p{margin-top:9px}
.lh-bullets{display:flex;gap:36px;margin-top:10px}
.lh-bullets ul{padding-left:10px;width:110px}
.lh-sign{margin-top:16px}
.lh-sign svg{display:block;margin:6px 0 2px}
.lh-foot{position:absolute;left:0;bottom:0;width:100%;height:38px;background:var(--navy);color:#fff;font-size:6px;display:flex;align-items:center;gap:26px;padding-left:30px}
.lh-foot span{display:flex;align-items:center;gap:5px}
.lh-corner{position:absolute;right:0;bottom:0;width:30px;height:38px;background:var(--grey)}
.lh-page{position:absolute;right:44px;bottom:50px;font-size:6px;color:#56606c}
</style>
</head>
<body>

<!-- Row 1 -->
<svg class="slide light" viewBox="0 0 265 150" style="left:53px;top:117px">
  <defs><linearGradient id="chevA" x1="0" x2="1"><stop offset="0" stop-color="#1d2f45"/><stop offset="1" stop-color="#566476"/></linearGradient></defs>
  <rect width="265" height="150" fill="var(--navy)"/>
  <rect x="170" width="95" height="150" fill="url(#chevA)" role="img" aria-label="Faint angled decoration"/>
  <line x1="32" y1="62" x2="32" y2="92" stroke="#fff" stroke-width=".6"/>
  <text class="mark" x="105" y="70" text-anchor="middle" font-size="17" letter-spacing="1.5">KORVATH</text>
  <text x="105" y="81" text-anchor="middle" font-size="4.2" letter-spacing=".3">ADVISORY FOR BOARDS,</text>
  <text x="105" y="87" text-anchor="middle" font-size="4.2" letter-spacing=".3">OWNERS &amp; EXECUTIVE TEAMS</text>
  <text class="sm" x="18" y="102">Business</text><text class="sm" x="18" y="107">Presentation</text><text class="sm" x="18" y="112">Template</text>
  <text class="lb" x="218" y="104">WE DO:</text>
  <text class="xs" x="218" y="110">CFOs</text><text class="xs" x="218" y="114">Real Estate</text><text class="xs" x="218" y="118">Tax Advisors</text>
</svg>

<svg class="slide light" viewBox="0 0 265 150" style="left:235px;top:117px">
  <defs><linearGradient id="chevB" x1="0" x2="1"><stop offset="0" stop-color="#1d2f45"/><stop offset=".6" stop-color="#6b6a5c"/><stop offset="1" stop-color="#3a4556"/></linearGradient></defs>
  <rect width="265" height="150" fill="var(--navy)"/>
  <rect x="170" width="95" height="150" fill="url(#chevB)" role="img" aria-label="Faint angled decoration with gold edge"/>
  <line x1="32" y1="62" x2="32" y2="92" stroke="#fff" stroke-width=".6"/>
  <text class="mark" x="105" y="70" text-anchor="middle" font-size="17" letter-spacing="1.5" style="fill:var(--gold)">KORVATH</text>
  <text x="105" y="81" text-anchor="middle" font-size="4.2" letter-spacing=".3">ADVISORY FOR BOARDS,</text>
  <text x="105" y="87" text-anchor="middle" font-size="4.2" letter-spacing=".3">OWNERS &amp; EXECUTIVE TEAMS</text>
  <text class="sm" x="18" y="102">Business</text><text class="sm" x="18" y="107">Presentation</text><text class="sm" x="18" y="112">Template</text>
  <text class="lb" x="218" y="104">WE DO:</text>
  <text class="xs" x="218" y="110">CFOs</text><text class="xs" x="218" y="114">Real Estate</text><text class="xs" x="218" y="118">Tax Advisors</text>
</svg>

<svg class="slide light" viewBox="0 0 265 150" style="left:417px;top:117px">
  <rect width="265" height="150" fill="var(--navy)"/>
  <line x1="32" y1="62" x2="32" y2="92" stroke="#fff" stroke-width=".6"/>
  <text class="mark" x="132" y="66" text-anchor="middle" font-size="17" letter-spacing="1.5">KORVATH</text>
  <text x="132" y="76" text-anchor="middle" font-size="4.2" letter-spacing=".3">ADVISORY FOR BOARDS</text>
  <text x="132" y="82" text-anchor="middle" font-size="4.2" letter-spacing=".3">OWNERS &amp; EXECUTIVE TEAMS</text>
  <text class="sm" x="18" y="102">Business</text><text class="sm" x="18" y="107">Presentation</text><text class="sm" x="18" y="112">Template</text>
  <text class="lb" x="218" y="104">WE DO:</text>
  <text class="xs" x="218" y="110">CFOs</text><text class="xs" x="218" y="114">Real Estate</text><text class="xs" x="218" y="118">Tax Advisors</text>
</svg>

<svg class="slide light" viewBox="0 0 265 150" style="left:597px;top:117px">
  <rect width="265" height="150" fill="var(--charcoal)"/>
  <text class="lb" x="30" y="22">INTRODUCTION</text><text class="lb" x="228" y="22">KORVATH</text>
  <text class="tt" x="30" y="36">Presentation</text><text class="tt" x="30" y="48">Agenda</text>
  <line x1="30" y1="74" x2="30" y2="118" stroke="#9a9c9f" stroke-width=".6"/>
  <g class="num"><text x="42" y="88" style="fill:#a4a6a9">01</text><text x="112" y="88" style="fill:#a4a6a9">02</text><text x="183" y="88" style="fill:#a4a6a9">03</text>
  <text x="42" y="114" style="fill:#a4a6a9">04</text><text x="112" y="114" style="fill:#a4a6a9">05</text><text x="183" y="114" style="fill:#a4a6a9">06</text></g>
  <text class="xs" x="65" y="83">About Us</text><text class="xs" x="135" y="83">Who We Are?</text><text class="xs" x="206" y="83">What We Do?</text>
  <text class="xs" x="65" y="109">Our Works</text><text class="xs" x="135" y="109">Project Timeline</text><text class="xs" x="206" y="109">Some Analysis</text>
</svg>

<svg class="slide" viewBox="0 0 265 150" style="left:779px;top:117px">
  <rect width="265" height="150" fill="var(--paper)"/>
  <text class="lb" x="30" y="22">INTRODUCTION</text>
  <text class="tt" x="30" y="36">Executive</text><text class="tt" x="30" y="48">summary</text>
  <g class="bar"><rect x="30" y="62" width="80" height="1.4"/><rect x="30" y="67" width="76" height="1.4"/><rect x="30" y="72" width="80" height="1.4"/><rect x="30" y="77" width="70" height="1.4"/><rect x="30" y="86" width="80" height="1.4"/><rect x="30" y="91" width="74" height="1.4"/><rect x="30" y="96" width="62" height="1.4"/>
  <rect x="135" y="62" width="100" height="1.4"/><rect x="135" y="67" width="96" height="1.4"/><rect x="135" y="72" width="100" height="1.4"/><rect x="135" y="77" width="88" height="1.4"/><rect x="135" y="86" width="100" height="1.4"/><rect x="135" y="91" width="92" height="1.4"/><rect x="135" y="96" width="100" height="1.4"/><rect x="135" y="101" width="70" height="1.4"/></g>
  <text class="ft" x="17" y="143">KORVATH</text>
</svg>

<svg class="slide light" viewBox="0 0 265 150" style="left:961px;top:117px">
  <rect width="265" height="150" fill="var(--navy)"/>
  <text class="lb" x="30" y="22">INTRODUCTION</text>
  <text class="tt" x="30" y="36">About Korvath</text><text class="tt" x="30" y="48">Management</text>
  <g fill="none" stroke="#fff" stroke-width=".7"><rect x="30" y="62" width="8" height="8"/><rect x="30" y="85" width="8" height="8"/><rect x="30" y="108" width="8" height="8"/></g>
  <g class="dbar"><rect x="50" y="62" width="190" height="1.3"/><rect x="50" y="66" width="180" height="1.3"/><rect x="50" y="70" width="120" height="1.3"/>
  <rect x="50" y="85" width="190" height="1.3"/><rect x="50" y="89" width="185" height="1.3"/><rect x="50" y="93" width="110" height="1.3"/>
  <rect x="50" y="108" width="190" height="1.3"/><rect x="50" y="112" width="175" height="1.3"/><rect x="50" y="116" width="100" height="1.3"/></g>
  <text class="ft" x="17" y="143">KORVATH</text>
</svg>

<!-- Row 2 -->
<svg class="slide" viewBox="0 0 265 150" style="left:53px;top:229px">
  <rect width="265" height="150" fill="var(--paper)"/>
  <rect x="192" width="73" height="150" fill="var(--navy)"/>
  <text class="mark" transform="translate(236 112) rotate(-90)" font-size="14" letter-spacing="2" style="fill:#5c6c80">KORVATH</text>
  <line x1="5" y1="32" x2="26" y2="32" stroke="var(--navy)" stroke-width=".6"/>
  <text class="lb" x="30" y="22">INTRODUCTION</text>
  <text class="tt" x="30" y="36">About</text><text class="tt" x="30" y="48">Us</text>
  <g class="bar"><rect x="30" y="66" width="130" height="1.4"/><rect x="30" y="71" width="124" height="1.4"/><rect x="30" y="76" width="130" height="1.4"/><rect x="30" y="81" width="96" height="1.4"/><rect x="30" y="92" width="130" height="1.4"/><rect x="30" y="97" width="120" height="1.4"/><rect x="30" y="102" width="130" height="1.4"/><rect x="30" y="107" width="84" height="1.4"/></g>
  <text class="ft" x="17" y="143">KORVATH</text>
</svg>

<svg class="slide" viewBox="0 0 265 150" style="left:235px;top:229px">
  <rect width="265" height="150" fill="var(--paper)"/>
  <line x1="5" y1="32" x2="26" y2="32" stroke="var(--navy)" stroke-width=".6"/>
  <text class="lb" x="30" y="22">INTRODUCTION</text>
  <text class="tt" x="30" y="36">The Problem</text>
  <rect x="108" y="62" width="64" height="66" fill="var(--charcoal)"/>
  <text class="xs w" x="114" y="72">Title Goes Here</text>
  <g style="fill:#7b7d80"><rect x="114" y="78" width="50" height="1.2"/><rect x="114" y="82" width="46" height="1.2"/><rect x="114" y="86" width="50" height="1.2"/><rect x="114" y="90" width="40" height="1.2"/></g>
  <g class="bar"><rect x="30" y="64" width="66" height="1.4"/><rect x="30" y="69" width="62" height="1.4"/><rect x="30" y="74" width="66" height="1.4"/><rect x="30" y="79" width="50" height="1.4"/><rect x="30" y="90" width="66" height="1.4"/><rect x="30" y="95" width="60" height="1.4"/>
  <rect x="185" y="64" width="64" height="1.4"/><rect x="185" y="69" width="60" height="1.4"/><rect x="185" y="74" width="64" height="1.4"/><rect x="185" y="79" width="48" height="1.4"/><rect x="185" y="90" width="64" height="1.4"/><rect x="185" y="95" width="56" height="1.4"/></g>
  <text class="ft" x="17" y="143">KORVATH</text>
</svg>

<svg class="slide light" viewBox="0 0 265 150" style="left:417px;top:229px">
  <rect width="265" height="150" fill="var(--paper)"/>
  <rect x="128" width="137" height="150" fill="var(--navy)"/>
  <line x1="5" y1="67" x2="26" y2="67" stroke="var(--navy)" stroke-width=".6"/>
  <text class="lb" x="30" y="57" style="fill:var(--navy)">INTRODUCTION</text>
  <text class="tt" x="30" y="71" style="fill:var(--navy)">Presentation</text><text class="tt" x="30" y="83" style="fill:var(--navy)">Targets</text>
  <text class="num" x="142" y="34">01</text><text class="num" x="142" y="64">02</text><text class="num" x="142" y="94">03</text><text class="num" x="142" y="124">04</text>
  <text class="xs" x="168" y="24">Your Title Goes Here</text><text class="xs" x="168" y="54">Your Title Goes Here</text><text class="xs" x="168" y="84">Your Title Goes Here</text><text class="xs" x="168" y="114">Your Title Goes Here</text>
  <g class="dbar"><rect x="168" y="28" width="75" height="1.2"/><rect x="168" y="32" width="60" height="1.2"/><rect x="168" y="58" width="75" height="1.2"/><rect x="168" y="62" width="60" height="1.2"/><rect x="168" y="88" width="75" height="1.2"/><rect x="168" y="92" width="60" height="1.2"/><rect x="168" y="118" width="75" height="1.2"/><rect x="168" y="122" width="60" height="1.2"/></g>
  <text class="ft" x="17" y="143" style="fill:var(--navy)">KORVATH</text>
</svg>

<svg class="slide" viewBox="0 0 265 150" style="left:597px;top:229px">
  <rect width="265" height="150" fill="var(--paper)"/>
  <line x1="5" y1="32" x2="26" y2="32" stroke="var(--navy)" stroke-width=".6"/>
  <text class="lb" x="30" y="22">INTRODUCTION</text>
  <text class="tt" x="30" y="36">Some Facts</text><text class="tt" x="30" y="48">About US</text>
  <g fill="none" stroke="var(--navy)" stroke-width=".7"><path d="M54 66 l8 -3 l-3 8 l-1 -4 z"/><circle cx="111" cy="67" r="3"/><rect x="164" y="64" width="8" height="6"/><path d="M220 63 h6 v3 a3 3 0 0 1 -6 0 z M223 69 v3"/></g>
  <rect x="30" y="78" width="220" height="20" fill="var(--navy)"/>
  <g><text class="w num" x="58" y="93" text-anchor="middle">250</text><text class="w num" x="113" y="93" text-anchor="middle">1.2K</text><text class="w num" x="168" y="93" text-anchor="middle">4.3M</text><text class="w num" x="223" y="93" text-anchor="middle">16</text></g>
  <g stroke="var(--navy)" stroke-width=".5"><line x1="58" y1="99" x2="58" y2="106"/><line x1="113" y1="99" x2="113" y2="106"/><line x1="168" y1="99" x2="168" y2="106"/><line x1="223" y1="99" x2="223" y2="106"/></g>
  <text class="xs" x="58" y="112" text-anchor="middle">Projects Done</text><text class="xs" x="113" y="112" text-anchor="middle">Happy Clients</text><text class="xs" x="168" y="112" text-anchor="middle">Earned</text><text class="xs" x="223" y="112" text-anchor="middle">Awards</text>
  <text class="ft" x="17" y="143">KORVATH</text>
</svg>

<svg class="slide light" viewBox="0 0 265 150" style="left:779px;top:229px">
  <rect width="265" height="150" fill="var(--navy)"/>
  <rect x="20" y="28" width="130" height="92" fill="var(--grey)"/>
  <line x1="5" y1="64" x2="44" y2="64" stroke="#fff" stroke-width=".6"/>
  <text class="lb" x="48" y="52">ABOUT US</text>
  <text class="tt" x="48" y="66">Our</text><text class="tt" x="48" y="78">Culture</text>
  <g fill="#b0b2b5"><rect x="48" y="96" width="90" height="1.2"/><rect x="48" y="100" width="86" height="1.2"/><rect x="48" y="104" width="70" height="1.2"/></g>
  <text class="mark" transform="translate(236 112) rotate(-90)" font-size="14" letter-spacing="2" style="fill:#5c6c80">KORVATH</text>
  <text class="ft" x="17" y="143">KORVATH</text>
</svg>

<svg class="slide" viewBox="0 0 265 150" style="left:961px;top:229px">
  <rect width="265" height="150" fill="var(--paper)"/>
  <line x1="5" y1="32" x2="26" y2="32" stroke="var(--navy)" stroke-width=".6"/>
  <text class="lb" x="30" y="22">ABOUT US</text>
  <text class="tt" x="30" y="36">Why</text><text class="tt" x="30" y="48">Choose US?</text>
  <g class="bar"><rect x="30" y="62" width="80" height="1.4"/><rect x="30" y="67" width="74" height="1.4"/><rect x="30" y="72" width="80" height="1.4"/><rect x="30" y="77" width="56" height="1.4"/></g>
  <g fill="none" stroke="var(--navy)" stroke-width=".7"><path d="M147 38 l6 0 l2 3 l-5 5 l-5 -5 z"/><circle cx="207" cy="41" r="3.5"/><rect x="146" y="92" width="7" height="6" transform="rotate(20 150 95)"/><path d="M203 98 l8 -4 l-3 8 z"/></g>
  <text class="sm" x="145" y="54">Reliability</text><text class="sm" x="202" y="54">Efficiency</text><text class="sm" x="145" y="110">Quality</text><text class="sm" x="202" y="110">Delivery</text>
  <g class="bar"><rect x="145" y="58" width="42" height="1.2"/><rect x="145" y="62" width="38" height="1.2"/><rect x="145" y="66" width="42" height="1.2"/><rect x="202" y="58" width="42" height="1.2"/><rect x="202" y="62" width="38" height="1.2"/><rect x="202" y="66" width="42" height="1.2"/>
  <rect x="145" y="114" width="42" height="1.2"/><rect x="145" y="118" width="38" height="1.2"/><rect x="145" y="122" width="42" height="1.2"/><rect x="202" y="114" width="42" height="1.2"/><rect x="202" y="118" width="38" height="1.2"/><rect x="202" y="122" width="42" height="1.2"/></g>
  <text class="ft" x="17" y="143">KORVATH</text>
</svg>

<!-- Row 3 -->
<svg class="slide" viewBox="0 0 265 150" style="left:53px;top:338px">
  <rect width="265" height="150" fill="var(--paper)"/>
  <line x1="5" y1="32" x2="26" y2="32" stroke="var(--navy)" stroke-width=".6"/>
  <text class="lb" x="30" y="22">ABOUT US</text>
  <text class="tt" x="30" y="36">Our</text><text class="tt" x="30" y="48">Services</text>
  <g class="bar"><rect x="30" y="62" width="76" height="1.4"/><rect x="30" y="67" width="70" height="1.4"/><rect x="30" y="72" width="76" height="1.4"/><rect x="30" y="77" width="56" height="1.4"/></g>
  <g fill="none" stroke="var(--navy)" stroke-width=".7"><rect x="150" y="16" width="8" height="7"/><circle cx="219" cy="20" r="3.5"/><circle cx="154" cy="62" r="3.5"/><rect x="215" y="58" width="8" height="7"/><rect x="150" y="100" width="8" height="7"/><rect x="215" y="100" width="8" height="7"/></g>
  <text class="sm" x="154" y="30" text-anchor="middle">Photography</text><text class="sm" x="219" y="30" text-anchor="middle">Social Media</text>
  <text class="sm" x="154" y="73" text-anchor="middle">Web Development</text><text class="sm" x="219" y="73" text-anchor="middle">Printing</text>
  <text class="sm" x="154" y="115" text-anchor="middle">Video Editing</text><text class="sm" x="219" y="115" text-anchor="middle">Marketing</text>
  <g class="bar"><rect x="134" y="33" width="40" height="1.1"/><rect x="199" y="33" width="40" height="1.1"/><rect x="134" y="76" width="40" height="1.1"/><rect x="199" y="76" width="40" height="1.1"/><rect x="134" y="118" width="40" height="1.1"/><rect x="199" y="118" width="40" height="1.1"/></g>
  <text class="ft" x="17" y="143">KORVATH</text>
</svg>

<svg class="slide light" viewBox="0 0 265 150" style="left:235px;top:338px">
  <rect width="265" height="150" fill="var(--navy)"/>
  <line x1="0" y1="75" x2="265" y2="75" stroke="#4c5d72" stroke-width=".6"/>
  <g font-size="9" font-weight="300"><text x="42" y="50" text-anchor="middle" style="fill:#5c6c80">02</text><text x="102" y="50" text-anchor="middle" style="fill:#5c6c80">03</text><text x="162" y="50" text-anchor="middle" style="fill:#5c6c80">04</text><text x="222" y="50" text-anchor="middle" style="fill:#5c6c80">05</text></g>
  <g fill="var(--grey)"><circle cx="42" cy="75" r="19"/><circle cx="102" cy="75" r="19"/><circle cx="162" cy="75" r="19"/><circle cx="222" cy="75" r="19"/></g>
  <g fill="none" stroke="#fff" stroke-width=".8"><circle cx="42" cy="73" r="5"/><path d="M96 69 l12 12 M108 69 l-12 12"/><path d="M159 81 h7 l-2 -7 a3 3 0 1 0 -4 -2 z"/><path d="M216 81 l10 -10 l1 3 l-8 8 z"/></g>
  <text class="sm" x="42" y="106" text-anchor="middle">Ideate</text><text class="sm" x="102" y="106" text-anchor="middle">Prototype</text><text class="sm" x="162" y="106" text-anchor="middle">Strategize</text><text class="sm" x="222" y="106" text-anchor="middle">Build &amp; Execute</text>
  <g class="dbar"><rect x="26" y="111" width="32" height="1.1"/><rect x="86" y="111" width="32" height="1.1"/><rect x="146" y="111" width="32" height="1.1"/><rect x="206" y="111" width="32" height="1.1"/></g>
  <text class="ft" x="17" y="143">KORVATH</text>
</svg>

<svg class="slide" viewBox="0 0 265 150" style="left:417px;top:338px">
  <rect width="265" height="150" fill="var(--paper)"/>
  <line x1="5" y1="32" x2="26" y2="32" stroke="var(--navy)" stroke-width=".6"/>
  <text class="lb" x="30" y="22">PROJECT</text>
  <text class="tt" x="30" y="36">Approach</text>
  <circle cx="150" cy="80" r="29" fill="none" stroke="var(--navy)" stroke-width="12"/>
  <circle cx="150" cy="80" r="29" fill="none" stroke="var(--grey)" stroke-width="12" stroke-dasharray="45 137" transform="rotate(-180 150 80)"/>
  <text class="xs" x="150" y="81" text-anchor="middle" font-weight="700">APPROACH</text>
  <text class="sm" x="104" y="54" text-anchor="end">Startup</text><text class="sm" x="196" y="54">Startup</text><text class="sm" x="104" y="110" text-anchor="end">Startup</text><text class="sm" x="196" y="110">Startup</text>
  <g class="bar"><rect x="64" y="58" width="40" height="1.1"/><rect x="68" y="62" width="36" height="1.1"/><rect x="196" y="58" width="40" height="1.1"/><rect x="196" y="62" width="36" height="1.1"/><rect x="64" y="114" width="40" height="1.1"/><rect x="68" y="118" width="36" height="1.1"/><rect x="196" y="114" width="40" height="1.1"/><rect x="196" y="118" width="36" height="1.1"/></g>
  <text class="ft" x="17" y="143">KORVATH</text>
</svg>

<svg class="slide" viewBox="0 0 265 150" style="left:597px;top:338px">
  <rect width="265" height="150" fill="var(--paper)"/>
  <line x1="5" y1="32" x2="26" y2="32" stroke="var(--navy)" stroke-width=".6"/>
  <text class="lb" x="30" y="22">PROJECT</text>
  <text class="tt" x="30" y="36">Project</text><text class="tt" x="30" y="48">Invoice</text>
  <text class="sm" x="30" y="66">$14,300</text><text class="xs" x="30" y="71">USD Dollar Only</text>
  <g class="bar"><rect x="30" y="76" width="64" height="1.2"/><rect x="30" y="80" width="60" height="1.2"/><rect x="30" y="84" width="64" height="1.2"/><rect x="30" y="88" width="48" height="1.2"/></g>
  <rect x="108" y="18" width="140" height="10" fill="var(--navy)"/>
  <text class="xs w" x="112" y="24.5">NO</text><text class="xs w" x="124" y="24.5">DESCRIPTION</text><text class="xs w" x="195" y="24.5">UNIT PRICE</text><text class="xs w" x="222" y="24.5">TOTAL</text>
  <g stroke="#e2e4e7" stroke-width=".5"><line x1="108" y1="42" x2="248" y2="42"/><line x1="108" y1="56" x2="248" y2="56"/><line x1="108" y1="70" x2="248" y2="70"/><line x1="108" y1="84" x2="248" y2="84"/></g>
  <g class="bar"><rect x="124" y="34" width="40" height="1.2"/><rect x="124" y="48" width="36" height="1.2"/><rect x="124" y="62" width="30" height="1.2"/><rect x="124" y="76" width="34" height="1.2"/><rect x="225" y="34" width="14" height="1.2"/><rect x="225" y="48" width="14" height="1.2"/><rect x="225" y="62" width="14" height="1.2"/><rect x="225" y="76" width="14" height="1.2"/></g>
  <rect x="108" y="90" width="140" height="9" fill="var(--mist)"/>
  <text class="xs" x="192" y="96">Sub Total</text><text class="xs" x="225" y="96">$9,500</text>
  <text class="xs" x="192" y="108">Tax</text><text class="xs" x="225" y="108">$4,800</text>
  <rect x="108" y="114" width="140" height="10" fill="var(--charcoal)"/>
  <text class="xs w" x="188" y="120.5">Grand Total</text><text class="xs w" x="225" y="120.5">$14,300</text>
  <text class="ft" x="17" y="143">KORVATH</text>
</svg>

<svg class="slide light" viewBox="0 0 265 150" style="left:779px;top:338px">
  <rect width="265" height="150" fill="var(--navy)"/>
  <line x1="5" y1="32" x2="26" y2="32" stroke="#fff" stroke-width=".6"/>
  <text class="lb" x="30" y="22">INTRODUCTION</text>
  <text class="tt" x="30" y="36">About</text><text class="tt" x="30" y="48">US</text>
  <g class="dbar"><rect x="30" y="62" width="66" height="1.2"/><rect x="30" y="66" width="62" height="1.2"/><rect x="30" y="70" width="66" height="1.2"/><rect x="30" y="74" width="50" height="1.2"/></g>
  <rect x="120" y="26" width="125" height="82" rx="20" fill="#c9ced5" role="img" aria-label="Map of Australia divided into states"/>
  <text class="num" x="30" y="115">+4.3K</text><text class="num" x="92" y="115">+26K</text>
  <text class="xs" x="30" y="122">New Customers</text><text class="xs" x="92" y="122">New Subscribers</text>
  <text class="ft" x="17" y="143">KORVATH</text>
</svg>

<svg class="slide" viewBox="0 0 265 150" style="left:961px;top:338px">
  <defs><linearGradient id="mapG" x1="0" x2="1"><stop offset="0" stop-color="#1d2f45"/><stop offset=".5" stop-color="#dfe1e4"/><stop offset="1" stop-color="#5a5c60"/></linearGradient></defs>
  <rect width="265" height="150" fill="var(--paper)"/>
  <line x1="5" y1="32" x2="26" y2="32" stroke="var(--navy)" stroke-width=".6"/>
  <text class="lb" x="30" y="22">MAPS</text>
  <text class="tt" x="30" y="36">Australia</text><text class="tt" x="30" y="48">Analysis</text>
  <rect x="110" y="48" width="92" height="70" rx="18" fill="url(#mapG)" role="img" aria-label="Map of Australia with highlighted states"/>
  <text x="200" y="38" font-size="11" font-weight="300">14.2K</text><text class="xs" x="200" y="44">Lorem State</text>
  <text x="62" y="88" font-size="11" font-weight="300">22.3K</text><text class="xs" x="64" y="94">Lorem State</text>
  <line x1="88" y1="100" x2="112" y2="96" stroke="var(--navy)" stroke-width=".5"/>
  <text class="ft" x="17" y="143">KORVATH</text>
</svg>

<!-- Row 4 -->
<svg class="slide" viewBox="0 0 265 150" style="left:53px;top:445px">
  <rect width="265" height="150" fill="var(--paper)"/>
  <line x1="5" y1="32" x2="26" y2="32" stroke="var(--navy)" stroke-width=".6"/>
  <text class="lb" x="30" y="22">PROJECT</text>
  <text class="tt" x="30" y="36">Project</text><text class="tt" x="30" y="48">Status</text>
  <rect x="30" y="62" width="218" height="10" fill="var(--navy)"/>
  <text class="xs w" x="34" y="68.5">PROJECT PROCESS</text><text class="xs w" x="100" y="68.5">CUSTOMER</text><text class="xs w" x="126" y="68.5">MANAGER</text><text class="xs w" x="154" y="68.5">DESIGN</text><text class="xs w" x="184" y="68.5">DEV TEAM</text><text class="xs w" x="216" y="68.5">MARKETING</text>
  <g class="bar"><rect x="34" y="79" width="40" height="1.2"/><rect x="34" y="91" width="44" height="1.2"/><rect x="34" y="103" width="36" height="1.2"/><rect x="34" y="115" width="42" height="1.2"/></g>
  <g fill="none" stroke="var(--grey)" stroke-width=".5"><circle cx="108" cy="80" r="2.5"/><circle cx="135" cy="80" r="2.5"/><circle cx="160" cy="80" r="2.5"/><circle cx="108" cy="92" r="2.5"/><circle cx="135" cy="92" r="2.5"/><circle cx="160" cy="92" r="2.5"/><circle cx="135" cy="104" r="2.5"/><circle cx="160" cy="104" r="2.5"/><circle cx="192" cy="104" r="2.5"/><circle cx="224" cy="104" r="2.5"/><circle cx="135" cy="116" r="2.5"/><circle cx="192" cy="116" r="2.5"/><circle cx="224" cy="116" r="2.5"/></g>
  <text class="ft" x="17" y="143">KORVATH</text>
</svg>

<svg class="slide" viewBox="0 0 265 150" style="left:235px;top:445px">
  <rect width="265" height="150" fill="var(--paper)"/>
  <line x1="5" y1="32" x2="26" y2="32" stroke="var(--navy)" stroke-width=".6"/>
  <text class="lb" x="30" y="22">PROJECT</text>
  <text class="tt" x="30" y="36">Packages</text><text class="tt" x="30" y="48">Price</text>
  <text class="sm" x="30" y="66">Starting from</text><text class="sm" x="30" y="71">$25 Monthly</text>
  <g class="bar"><rect x="30" y="76" width="58" height="1.2"/><rect x="30" y="80" width="54" height="1.2"/><rect x="30" y="84" width="58" height="1.2"/><rect x="30" y="88" width="44" height="1.2"/>
  <rect x="108" y="34" width="32" height="1.2"/><rect x="108" y="46" width="28" height="1.2"/><rect x="108" y="58" width="34" height="1.2"/><rect x="108" y="70" width="30" height="1.2"/><rect x="108" y="82" width="26" height="1.2"/><rect x="108" y="94" width="32" height="1.2"/><rect x="108" y="106" width="28" height="1.2"/></g>
  <rect x="155" y="18" width="93" height="9" fill="var(--navy)"/>
  <text class="xs w" x="170" y="24" text-anchor="middle">BASIC</text><text class="xs w" x="201" y="24" text-anchor="middle">STANDARD</text><text class="xs w" x="232" y="24" text-anchor="middle">PRO</text>
  <g fill="none" stroke="var(--navy)" stroke-width=".5"><path d="M168 70 l1.5 1.5 l3 -3 M199 70 l1.5 1.5 l3 -3 M230 70 l1.5 1.5 l3 -3 M199 94 l1.5 1.5 l3 -3 M230 94 l1.5 1.5 l3 -3 M230 106 l1.5 1.5 l3 -3 M168 81 l4 4 M172 81 l-4 4 M168 105 l4 4 M172 105 l-4 4"/></g>
  <rect x="155" y="114" width="93" height="10" fill="var(--charcoal)"/>
  <text class="xs w" x="170" y="120.5" text-anchor="middle">$25/month</text><text class="xs w" x="201" y="120.5" text-anchor="middle">$80/month</text><text class="xs w" x="232" y="120.5" text-anchor="middle">$120/month</text>
  <text class="ft" x="17" y="143">KORVATH</text>
</svg>

<svg class="slide" viewBox="0 0 265 150" style="left:417px;top:445px">
  <rect width="265" height="150" fill="var(--paper)"/>
  <line x1="5" y1="32" x2="26" y2="32" stroke="var(--navy)" stroke-width=".6"/>
  <text class="lb" x="30" y="22">PROJECT</text>
  <text class="tt" x="30" y="36">Project</text><text class="tt" x="30" y="48">Schedule</text>
  <text class="sm" x="30" y="60">Takes</text><text class="sm" x="30" y="65">5 Weeks</text>
  <g class="bar"><rect x="30" y="70" width="58" height="1.2"/><rect x="30" y="74" width="54" height="1.2"/><rect x="30" y="78" width="58" height="1.2"/></g>
  <rect x="107" y="18" width="141" height="8" fill="var(--navy)"/>
  <text class="xs w" x="111" y="23.5">WORKS</text>
  <g class="xs"><text class="w" x="170" y="23.5">W1</text><text class="w" x="186" y="23.5">W2</text><text class="w" x="202" y="23.5">W3</text><text class="w" x="218" y="23.5">W4</text><text class="w" x="234" y="23.5">W5</text></g>
  <g class="bar"><rect x="110" y="32" width="30" height="1.1"/><rect x="110" y="44" width="24" height="1.1"/><rect x="110" y="56" width="36" height="1.1"/><rect x="110" y="68" width="32" height="1.1"/><rect x="110" y="80" width="28" height="1.1"/><rect x="110" y="92" width="22" height="1.1"/><rect x="110" y="104" width="30" height="1.1"/><rect x="110" y="116" width="26" height="1.1"/></g>
  <g fill="var(--navy)"><rect x="168" y="37" width="44" height="1.4"/><rect x="174" y="49" width="10" height="1.4"/><rect x="186" y="61" width="10" height="1.4"/><rect x="190" y="73" width="12" height="1.4"/><rect x="196" y="85" width="12" height="1.4"/><rect x="206" y="97" width="10" height="1.4"/><rect x="214" y="109" width="14" height="1.4"/><rect x="228" y="121" width="12" height="1.4"/></g>
  <text class="ft" x="17" y="143">KORVATH</text>
</svg>

<svg class="slide" viewBox="0 0 265 150" style="left:597px;top:445px">
  <rect width="265" height="150" fill="var(--paper)"/>
  <line x1="5" y1="32" x2="26" y2="32" stroke="var(--navy)" stroke-width=".6"/>
  <text class="lb" x="30" y="22">PROJECT</text>
  <text class="tt" x="30" y="36">Your Project</text><text class="tt" x="30" y="48">Description</text>
  <rect x="30" y="62" width="218" height="8" fill="var(--navy)"/>
  <g class="xs"><text class="w" x="34" y="67.5">DESCRIPTION</text><text class="w" x="90" y="67.5">2008</text><text class="w" x="112" y="67.5">2009</text><text class="w" x="134" y="67.5">2010</text><text class="w" x="156" y="67.5">2011</text><text class="w" x="178" y="67.5">2012</text><text class="w" x="200" y="67.5">2013</text><text class="w" x="222" y="67.5">2014</text></g>
  <g stroke="#e2e4e7" stroke-width=".5"><line x1="30" y1="80" x2="248" y2="80"/><line x1="30" y1="90" x2="248" y2="90"/><line x1="30" y1="100" x2="248" y2="100"/><line x1="30" y1="110" x2="248" y2="110"/></g>
  <g class="bar"><rect x="34" y="75" width="34" height="1.1"/><rect x="34" y="85" width="30" height="1.1"/><rect x="34" y="95" width="36" height="1.1"/><rect x="34" y="105" width="28" height="1.1"/></g>
  <rect x="30" y="114" width="218" height="7" fill="var(--charcoal)"/>
  <text class="xs w" x="34" y="119">Total Value</text>
  <text class="ft" x="17" y="143">KORVATH</text>
</svg>

<svg class="slide light" viewBox="0 0 265 150" style="left:779px;top:445px">
  <rect width="265" height="150" fill="var(--paper)"/>
  <line x1="5" y1="32" x2="26" y2="32" stroke="var(--navy)" stroke-width=".6"/>
  <text class="lb" x="30" y="22" style="fill:var(--navy)">ANALYSIS</text>
  <text class="tt" x="30" y="36" style="fill:var(--navy)">Market</text><text class="tt" x="30" y="48" style="fill:var(--navy)">Size</text>
  <g fill="var(--navy)"><circle cx="45" cy="90" r="10"/><circle cx="83" cy="86" r="14"/><circle cx="133" cy="82" r="19"/><circle cx="195" cy="75" r="25"/></g>
  <text x="45" y="93" text-anchor="middle" font-size="5" font-weight="300">$2.2M</text>
  <text x="83" y="90" text-anchor="middle" font-size="7" font-weight="300">$6 M</text>
  <text x="133" y="86" text-anchor="middle" font-size="9" font-weight="300">$10 K</text>
  <text x="195" y="80" text-anchor="middle" font-size="12" font-weight="300">$14 M</text>
  <text class="xs" x="195" y="66" text-anchor="middle" font-size="2.4">ONLINE SALES</text>
  <g class="bar"><rect x="30" y="120" width="218" height="1.1"/><rect x="50" y="124" width="178" height="1.1"/></g>
  <text class="ft" x="17" y="143" style="fill:var(--navy)">KORVATH</text>
</svg>

<svg class="slide" viewBox="0 0 265 150" style="left:961px;top:445px">
  <rect width="265" height="150" fill="var(--paper)"/>
  <line x1="5" y1="32" x2="26" y2="32" stroke="var(--navy)" stroke-width=".6"/>
  <text class="lb" x="30" y="22">ANALYSIS</text>
  <text class="tt" x="30" y="36">Comparison</text><text class="tt" x="30" y="48">Column Chart</text>
  <g class="bar"><rect x="30" y="62" width="70" height="1.2"/><rect x="30" y="66" width="66" height="1.2"/><rect x="30" y="70" width="70" height="1.2"/><rect x="30" y="74" width="50" height="1.2"/></g>
  <text class="xs" x="170" y="30" font-weight="700">What's going on Customers Mind</text>
  <g fill="var(--charcoal)"><rect x="142" y="46" width="5" height="70"/><rect x="180" y="42" width="5" height="74"/><rect x="216" y="56" width="5" height="60"/><rect x="234" y="56" width="5" height="60"/></g>
  <g fill="var(--grey)"><rect x="148" y="66" width="5" height="50"/><rect x="186" y="66" width="5" height="50"/><rect x="222" y="78" width="5" height="38"/></g>
  <g fill="var(--navy)"><rect x="154" y="74" width="5" height="42"/><rect x="192" y="80" width="5" height="36"/><rect x="198" y="60" width="5" height="56"/><rect x="240" y="66" width="5" height="50"/></g>
  <line x1="138" y1="116" x2="248" y2="116" stroke="var(--navy)" stroke-width=".4"/>
  <text class="xs" x="150" y="122" text-anchor="middle" font-size="2.4">Entertainment</text><text class="xs" x="192" y="122" text-anchor="middle" font-size="2.4">Holidays</text><text class="xs" x="232" y="122" text-anchor="middle" font-size="2.4">Social Media</text>
  <text class="ft" x="17" y="143">KORVATH</text>
</svg>

<!-- Row 5 -->
<svg class="slide" viewBox="0 0 265 150" style="left:53px;top:556px">
  <rect width="265" height="150" fill="var(--paper)"/>
  <line x1="5" y1="32" x2="26" y2="32" stroke="var(--navy)" stroke-width=".6"/>
  <text class="lb" x="30" y="22">ANALYSIS</text>
  <text class="tt" x="30" y="36">Comparison</text><text class="tt" x="30" y="48">Mountain Chart</text>
  <path d="M30 122 C44 122 48 74 56 74 C64 74 68 122 82 122 Z" fill="var(--navy)"/>
  <path d="M58 122 C72 122 76 86 84 86 C92 86 96 122 110 122 Z" fill="var(--grey)"/>
  <path d="M90 122 C104 122 108 74 116 74 C124 74 128 122 142 122 Z" fill="var(--navy)"/>
  <path d="M122 122 C136 122 140 88 148 88 C156 88 160 122 174 122 Z" fill="var(--grey)"/>
  <path d="M150 122 C164 122 168 58 176 58 C184 58 188 122 202 122 Z" fill="var(--navy)"/>
  <path d="M180 122 C194 122 198 74 206 74 C214 74 218 122 232 122 Z" fill="var(--grey)"/>
  <g class="xs"><text x="56" y="70" text-anchor="middle">$14M</text><text x="84" y="82" text-anchor="middle">$12M</text><text x="116" y="70" text-anchor="middle">$17M</text><text x="148" y="84" text-anchor="middle">$13M</text><text x="176" y="54" text-anchor="middle">$22M</text><text x="206" y="70" text-anchor="middle">$18M</text></g>
  <g class="xs" font-size="2.6"><text x="56" y="128" text-anchor="middle">Social</text><text x="88" y="128" text-anchor="middle">Forum</text><text x="116" y="128" text-anchor="middle">Network</text><text x="148" y="128" text-anchor="middle">Video</text><text x="176" y="128" text-anchor="middle">Stream</text><text x="206" y="128" text-anchor="middle">Photo</text></g>
  <text class="ft" x="17" y="143">KORVATH</text>
</svg>

<svg class="slide" viewBox="0 0 265 150" style="left:235px;top:556px">
  <rect width="265" height="150" fill="var(--paper)"/>
  <line x1="5" y1="32" x2="26" y2="32" stroke="var(--navy)" stroke-width=".6"/>
  <text class="lb" x="30" y="22">ANALYSIS</text>
  <text class="tt" x="30" y="36">Simple</text><text class="tt" x="30" y="48">Column Chart</text>
  <g fill="var(--navy)"><rect x="64" y="100" width="5" height="22"/><rect x="80" y="98" width="5" height="24"/><rect x="96" y="94" width="5" height="28"/><rect x="112" y="92" width="5" height="30"/><rect x="128" y="86" width="5" height="36"/><rect x="144" y="102" width="5" height="20"/><rect x="160" y="112" width="5" height="10"/><rect x="176" y="108" width="5" height="14"/><rect x="192" y="92" width="5" height="30"/><rect x="208" y="98" width="5" height="24"/><rect x="224" y="102" width="5" height="20"/><rect x="240" y="110" width="5" height="12"/></g>
  <g class="xs" font-size="2.4"><text x="66" y="97" text-anchor="middle">26,000</text><text x="98" y="91" text-anchor="middle">31,000</text><text x="130" y="83" text-anchor="middle">42,000</text><text x="162" y="109" text-anchor="middle">15,000</text><text x="194" y="89" text-anchor="middle">35,000</text><text x="226" y="99" text-anchor="middle">22,000</text></g>
  <text class="ft" x="17" y="143">KORVATH</text>
</svg>

<svg class="slide" viewBox="0 0 265 150" style="left:417px;top:556px">
  <rect width="265" height="150" fill="var(--paper)"/>
  <line x1="5" y1="32" x2="26" y2="32" stroke="var(--navy)" stroke-width=".6"/>
  <text class="lb" x="30" y="22">ANALYSIS</text>
  <text class="tt" x="30" y="36">Simple</text><text class="tt" x="30" y="48">Pie Chart</text>
  <g fill="none" stroke="var(--navy)" stroke-width=".6"><rect x="30" y="63" width="6" height="5"/><path d="M30 82 h6 M30 85 h6 M30 88 h6"/><rect x="30" y="101" width="6" height="6"/></g>
  <text class="sm" x="42" y="66">Branding &amp; Promotions</text><text class="sm" x="42" y="85">Analytics</text><text class="sm" x="42" y="104">SEO Services</text>
  <g class="bar"><rect x="42" y="69" width="50" height="1.1"/><rect x="42" y="72" width="44" height="1.1"/><rect x="42" y="88" width="50" height="1.1"/><rect x="42" y="91" width="44" height="1.1"/><rect x="42" y="107" width="50" height="1.1"/><rect x="42" y="110" width="44" height="1.1"/></g>
  <path d="M180 83 L180 53 A30 30 0 1 1 154.6 99 Z" fill="var(--navy)"/>
  <path d="M180 83 L154.6 99 A30 30 0 0 1 162.4 58.7 Z" fill="var(--grey)"/>
  <path d="M180 83 L162.4 58.7 A30 30 0 0 1 180 53 Z" fill="#c2c4c7"/>
  <text class="xs w" x="195" y="90">66%</text><text class="xs w" x="158" y="81">24%</text><text class="xs" x="172" y="62">10%</text>
  <text class="ft" x="17" y="143">KORVATH</text>
</svg>

<svg class="slide" viewBox="0 0 265 150" style="left:597px;top:556px">
  <rect width="265" height="150" fill="var(--paper)"/>
  <line x1="5" y1="32" x2="26" y2="32" stroke="var(--navy)" stroke-width=".6"/>
  <text class="lb" x="30" y="22">ANALYSIS</text>
  <text class="tt" x="30" y="36">Simple</text><text class="tt" x="30" y="48">Column Chart</text>
  <g fill="none" stroke="#e2e4e7" stroke-width="2"><circle cx="48" cy="83" r="14"/><circle cx="105" cy="83" r="14"/><circle cx="162" cy="83" r="14"/><circle cx="220" cy="83" r="14"/></g>
  <g fill="none" stroke="var(--navy)" stroke-width="2">
    <circle cx="48" cy="83" r="14" stroke-dasharray="72.2 88" transform="rotate(-90 48 83)"/>
    <circle cx="105" cy="83" r="14" stroke-dasharray="58 88" transform="rotate(-90 105 83)"/>
    <circle cx="162" cy="83" r="14" stroke-dasharray="48.4 88" transform="rotate(-90 162 83)"/>
    <circle cx="220" cy="83" r="14" stroke-dasharray="22.9 88" transform="rotate(-90 220 83)"/></g>
  <g font-size="7" font-weight="300"><text x="48" y="86" text-anchor="middle">82%</text><text x="105" y="86" text-anchor="middle">66%</text><text x="162" y="86" text-anchor="middle">55%</text><text x="220" y="86" text-anchor="middle">26%</text></g>
  <g stroke="var(--navy)" stroke-width=".5"><line x1="48" y1="99" x2="48" y2="104"/><line x1="105" y1="99" x2="105" y2="104"/><line x1="162" y1="99" x2="162" y2="104"/><line x1="220" y1="99" x2="220" y2="104"/></g>
  <g class="sm"><text x="48" y="110" text-anchor="middle">Texas</text><text x="105" y="110" text-anchor="middle">New York</text><text x="162" y="110" text-anchor="middle">Washington</text><text x="220" y="110" text-anchor="middle">Nevada</text></g>
  <text class="ft" x="17" y="143">KORVATH</text>
</svg>

<svg class="slide light" viewBox="0 0 265 150" style="left:779px;top:556px">
  <rect width="265" height="150" fill="var(--paper)"/>
  <rect x="160" width="105" height="150" fill="var(--navy)"/>
  <text x="30" y="56" font-size="10" font-weight="500" letter-spacing="3" style="fill:var(--navy)">CONTACT</text>
  <text x="30" y="72" font-size="10" font-weight="500" letter-spacing="3" style="fill:var(--navy)">US</text>
  <line x1="58" y1="68" x2="78" y2="68" stroke="var(--navy)" stroke-width=".8"/>
  <line x1="40" y1="88" x2="40" y2="106" stroke="var(--navy)" stroke-width=".6"/>
  <text class="xs" x="30" y="116" style="fill:var(--navy)">We will be waiting for your</text><text class="xs" x="30" y="120" style="fill:var(--navy)">nice comments and advices.</text>
  <g fill="none" stroke="#fff" stroke-width=".7"><path d="M178 30 q2 6 7 8 l2 -2 l-3 -2 l-1 1 q-2 -1 -3 -3 l1 -1 l-2 -3 z"/><rect x="177" y="62" width="9" height="6"/><path d="M177 62 l4.5 3.5 l4.5 -3.5"/><path d="M178 96 h7 v6 h-7 z M181 96 v-3 h4"/></g>
  <text class="sm" x="194" y="30">Call Us:</text><text class="xs" x="194" y="36">+00 123 456 789</text>
  <text class="sm" x="194" y="63">Email Us:</text><text class="xs" x="194" y="69">hello@korvath.example</text>
  <text class="sm" x="194" y="96">Follow Us:</text><text class="xs" x="194" y="102">@korvathadvisory</text>
</svg>

<!-- Brand headline -->
<div class="brand-block">
  <div class="brand-name">KORVATH</div>
  <div class="brand-tagline">ADVISORY FOR BOARDS,<br>OWNERS &amp; EXECUTIVE TEAMS</div>
  <div class="headline">Scriva Docs and Scriva<br>Slides template</div>
</div>
<div class="app-tiles">
  <div class="app-tile"><span class="dot"></span>Slides</div>
  <div class="app-tile"><span class="sq"></span>Docs</div>
</div>

<!-- Letterhead -->
<div class="letterhead">
  <div class="lh-head">
    <div class="lh-logo">
      <div class="name">KORVATH</div>
      <div class="tag">ADVISORY FOR BOARDS,<br>OWNERS &amp; EXECUTIVE TEAMS</div>
    </div>
    <div class="lh-person">
      <div class="pn">Dana Whitlow</div>
      <div class="pr">Chief Client Officer</div>
      <div class="ph"><svg width="7" height="7" viewBox="0 0 10 10"><path d="M1 1 q1 6 8 8 l0 -2.5 l-2.5 -1 l-1 1 q-2 -1 -3 -3 l1 -1 l-1 -2.5 z" fill="#fff"/></svg>+00 123 456 789</div>
    </div>
  </div>
  <div class="lh-body">
    <div class="lh-addr"><strong>Mr. Oliver Brennan</strong><br>Chief Executive Officer<br>14 Harlow Crescent<br>Eastvale WA 6190</div>
    <div class="lh-date">January 19, 2026</div>
    <p><strong>Dear Mr. Brennan</strong></p>
    <p>Eget est lorem ipsum dolor sit amet consectetur adipiscing. Quis auctor elit sed vulputate vitae mi sit amet mauris. In est quisquet ante in nibh. Sed risus pretium quam vulputate dignissim. Mi quis hendrerit dolor magna eget est lorem ipsum. Odio euismod lacinia at risus sed vulputate odio. Gravida cum sociis natoque penatibus et magnis dis parturient.</p>
    <p>Sit amet justo donec enim diam vulputate ut pharetra. Vitae congue mauris rhoncus aenean vel. Duis sed convallis et convallis tellus interdum velit. Odio morbi quis commodo odio aenean sed. Vitae aliquet nec ullamcorper sit amet risus nullam eget. Nec feugiat nisl pretium fusce id velit.</p>
    <p>Facilisis mauris sit amet massa. Tristique et sollicitudin quis in amet commodo et nulla facilisi nullam vehicula.</p>
    <div class="lh-bullets">
      <ul><li>Eget est lorem ipsum dolor sit amet consectetur adipiscing.</li><li>Quis auctor elit sed vulputate vitae mi sit amet mauris.</li></ul>
      <ul><li>Eget est lorem ipsum dolor sit amet consectetur adipiscing.</li><li>Quis auctor elit sed vulputate vitae mi sit amet mauris.</li></ul>
    </div>
    <div class="lh-sign">Sincerely Yours,
      <svg width="60" height="20" viewBox="0 0 60 20"><path d="M2 16 C10 4 16 4 14 14 C22 6 28 6 30 12 C36 4 44 6 58 2" fill="none" stroke="#26303c" stroke-width="1"/></svg>
      Mira Tallis<br>Executive Chair
    </div>
  </div>
  <div class="lh-page">P 02</div>
  <div class="lh-foot">
    <span><svg width="7" height="7" viewBox="0 0 10 10"><circle cx="5" cy="5" r="4" fill="none" stroke="#fff"/></svg>yourmail@domain.com</span>
    <span><svg width="6" height="8" viewBox="0 0 10 13"><path d="M5 12 C1 7 1 5 1 5 a4 4 0 0 1 8 0 C9 5 9 7 5 12 z" fill="#fff"/></svg>812 Ferrin Lane, SC</span>
  </div>
  <div class="lh-corner"></div>
</div>

</body>
</html>
```